Core Investment Strategy's Super Pie Chart

We need a one page visual explanation of an investment strategy we call "Hollis/Varrowby". This strategy emphasizes a "core" portfolio that will seldom change and "perimeter" investments that will change. Our investment management firm caters to wealthy individuals. We want to project an image of strength and reliability. At the same time, we are willing to explore new concepts. I have uploaded a PDF of my graphically-challenged assistant's attempt at creating the one page visual.

Investment

```html
<!DOCTYPE html>
<html lang="en">
<head>
<meta charset="utf-8">
<title>Hollis/Varrowby Portfolio</title>
<link rel="stylesheet" href="https://fonts.googleapis.com/css2?family=Barlow:wght@500;600;700&display=swap">
<style>
  :root {
    --navy: #0b2a57;
    --navy-mid: #16407a;
    --blue: #0a6db5;
    --green: #8cc540;
    --purple: #7b63a6;
    --crimson: #c6203f;
    --orange: #f07a1a;
    --yellow: #f6e11c;
    --ink: #1b2640;
    --white: #ffffff;
    --paper: #f3f3f4;
  }
  * { margin: 0; padding: 0; box-sizing: border-box; }
  html, body { width: 1200px; height: 848px; overflow: hidden; }
  body {
    font-family: "Barlow", Arial, sans-serif;
    background: radial-gradient(ellipse at 40% 45%, #ffffff 0%, #f1f1f2 55%, #dcdde0 100%);
    position: relative;
    color: var(--ink);
  }
  .frame { position: absolute; inset: 0; }
  .title {
    position: absolute; top: 26px; left: 0; width: 1200px;
    text-align: center; color: var(--white);
    font-weight: 700; font-size: 22px; letter-spacing: 0.5px;
  }
  .category {
    position: absolute; display: flex; align-items: flex-start; gap: 10px;
    font-weight: 600; font-size: 16px; line-height: 20px;
  }
  .swatch { width: 18px; height: 18px; flex: none; }
  .category--other { left: 93px; top: 134px; }
  .category--alt { left: 507px; top: 134px; }
  .category--core { left: 93px; top: 743px; }
  .category--funds { left: 507px; top: 743px; }
  .key {
    position: absolute; left: 863px; top: 322px; list-style: none;
  }
  .key li {
    display: flex; align-items: center; gap: 14px;
    font-weight: 600; font-size: 25px; height: 40px;
  }
  .key .swatch { width: 12px; height: 12px; }
  .slice-label {
    fill: var(--white); font-family: "Barlow", Arial, sans-serif;
    font-weight: 700; font-size: 14px; text-anchor: middle;
  }
  .slice-label--radial { font-size: 13px; }
</style>
</head>
<body>
<svg class="frame" width="1200" height="848" viewBox="0 0 1200 848">
  <defs>
    <linearGradient id="bandTop" x1="0" y1="0" x2="1" y2="0">
      <stop offset="0" stop-color="#0e3466"/>
      <stop offset="0.5" stop-color="#16457f"/>
      <stop offset="1" stop-color="#0a2650"/>
    </linearGradient>
    <linearGradient id="bandBottom" x1="0" y1="0" x2="1" y2="0">
      <stop offset="0" stop-color="#0a2650"/>
      <stop offset="0.5" stop-color="#1b4d8a"/>
      <stop offset="1" stop-color="#0a2650"/>
    </linearGradient>
    <linearGradient id="swoosh" x1="0" y1="0" x2="1" y2="0">
      <stop offset="0" stop-color="var(--orange)"/>
      <stop offset="0.35" stop-color="#f39a1c"/>
      <stop offset="0.7" stop-color="var(--yellow)"/>
      <stop offset="1" stop-color="var(--yellow)"/>
    </linearGradient>
  </defs>

  <!-- header band -->
  <path d="M0 0 H1200 V98 Q760 50 0 78 Z" fill="url(#bandTop)"/>
  <path d="M0 78 Q760 50 1200 98 V104 Q760 58 0 86 Z" fill="url(#swoosh)"/>

  <!-- footer band -->
  <path d="M0 800 Q300 770 620 790 Q950 810 1200 762 V848 H0 Z" fill="#b9cde4"/>
  <path d="M0 810 Q300 780 620 800 Q950 820 1200 772 V848 H0 Z" fill="url(#bandBottom)"/>

  <!-- perimeter rings -->
  <g class="perimeter">
    <path d="M139.4 387 A263 263 0 0 1 344 182.4 L344 215.2 A231 231 0 0 0 172.2 387 Z" fill="var(--purple)"/>
    <path d="M450 182.4 A263 263 0 0 1 654.6 387 L621.8 387 A231 231 0 0 0 450 215.2 Z" fill="var(--blue)"/>
    <path d="M344 697.6 A263 263 0 0 1 139.4 493 L172.2 493 A231 231 0 0 0 344 664.8 Z" fill="var(--green)"/>
    <path d="M654.6 493 A263 263 0 0 1 450 697.6 L450 664.8 A231 231 0 0 0 621.8 493 Z" fill="var(--crimson)"/>
  </g>

  <!-- core pie -->
  <g class="core" stroke="var(--white)" stroke-width="3" stroke-linejoin="round">
    <path d="M397 440 L397 235 A205 205 0 0 1 542 585 Z" fill="var(--blue)"/>
    <path d="M397 440 L542 585 A205 205 0 0 1 475.5 629.4 Z" fill="var(--blue)"/>
    <path d="M397 440 L475.5 629.4 A205 205 0 0 1 397 645 Z" fill="var(--blue)"/>
    <path d="M397 440 L397 645 A205 205 0 0 1 252 585 Z" fill="var(--blue)"/>
    <path d="M397 440 L252 585 A205 205 0 0 1 252 295 Z" fill="var(--green)"/>
    <path d="M397 440 L252 295 A205 205 0 0 1 397 235 Z" fill="var(--green)"/>
  </g>
  <circle cx="397" cy="440" r="26" fill="var(--white)"/>

  <text class="slice-label" x="513" y="398">Lg. Cap</text>
  <text class="slice-label" x="513" y="416">Equities,</text>
  <text class="slice-label" x="513" y="434">30%</text>

  <text class="slice-label slice-label--radial" transform="translate(464 540) rotate(56)" dy="4">Mid Cap Equities , 5%</text>

  <text class="slice-label" x="430" y="584">Sm.</text>
  <text class="slice-label" x="430" y="602">Cap</text>
  <text class="slice-label" x="430" y="620">Equities,</text>
  <text class="slice-label" x="430" y="638">5%</text>

  <text class="slice-label" x="345" y="555">Int'l/Dev.</text>
  <text class="slice-label" x="345" y="573">Equities,</text>
  <text class="slice-label" x="345" y="591">10%</text>

  <text class="slice-label" x="282" y="430">Intermediate</text>
  <text class="slice-label" x="282" y="448">Bonds,</text>
  <text class="slice-label" x="282" y="466">20%</text>

  <text class="slice-label" x="341" y="304">Short-Term</text>
  <text class="slice-label" x="341" y="322">Bonds,</text>
  <text class="slice-label" x="341" y="340">10%</text>
</svg>

<h1 class="title">HOLLIS/VARROWBY PORTFOLIO</h1>

<div class="category category--other"><span class="swatch" style="background:var(--purple)"></span><span>Other, 2%</span></div>
<div class="category category--alt"><span class="swatch" style="background:var(--blue)"></span><span>Alternative Assets, 7%</span></div>
<div class="category category--core"><span class="swatch" style="background:var(--green)"></span><span>Attractive Core Assets, 3%</span></div>
<div class="category category--funds"><span class="swatch" style="background:var(--crimson)"></span><span>Actively Managed Mutual<br>Funds, 8%</span></div>

<ul class="key">
  <li><span class="swatch" style="background:var(--blue)"></span>Lg. Cap Equities</li>
  <li><span class="swatch" style="background:var(--blue)"></span>Mid Cap Equities</li>
  <li><span class="swatch" style="background:var(--blue)"></span>Sm. Cap Equities</li>
  <li><span class="swatch" style="background:var(--blue)"></span>Int'l/Dev. Equities</li>
  <li><span class="swatch" style="background:var(--green)"></span>Intermediate&nbsp; Bonds</li>
  <li><span class="swatch" style="background:var(--green)"></span>Short-Term Bonds</li>
</ul>
</body>
</html>
```